We need business cards for our Kashmiri Indian Takeaway Shop. our business sells authentic Kashmiri Cuisine. We also offer catering services and have a BYO Function Room available for private bookings. We would like to see simple but stylish designs that feature Moroccan or Arabic style patterns/ borders and use golds, deep reds, pearl/cream and a touch of black or white. We do not want pictures of curries or Indian spices, chillies etc. The final design should communicate sumptuous, exotic dining.

Target Market(s)

Indian food lovers

Industry/Entity Type

Catering

Contact Information for Business Card

Rahim's Kitchen Authentic Kashmiri Indian Cuisine

Colors
ec2027
fce8d3
fcca95
faa54b

Requirements
Must have
• Simple but stylish design, using Moroccan/Arabic inspired borders or features
Should not have
• Pictures of curries, spices, food etc

```html
<!DOCTYPE html>
<html lang="en">
<head>
<meta charset="utf-8">
<title>Rahim's Kitchen – Business Card</title>
<link rel="stylesheet" href="https://fonts.googleapis.com/css2?family=Uncial+Antiqua&display=swap">
<style>
  :root {
    --backdrop: #e6e4e1;
    --gold-light: #f7df8c;
    --gold-mid: #ecc764;
    --gold-deep: #c9983a;
    --maroon: #6b1414;
    --ink: #1a1208;
    --ornament: #2a1c0c;
  }
  * { margin: 0; padding: 0; box-sizing: border-box; }
  html, body {
    width: 1200px;
    height: 800px;
    overflow: hidden;
    background: var(--backdrop);
  }
  .canvas {
    position: relative;
    width: 1200px;
    height: 800px;
  }
  .business-card {
    position: absolute;
    left: 100px;
    top: 110px;
    width: 1000px;
    height: 580px;
    background: linear-gradient(135deg, var(--gold-mid) 0%, var(--gold-light) 45%, var(--gold-mid) 75%, var(--gold-deep) 100%);
    box-shadow: 0 10px 30px rgba(0,0,0,0.18);
    overflow: hidden;
    font-family: "Uncial Antiqua", serif;
    color: var(--ink);
    text-transform: lowercase;
  }
  .band {
    position: absolute;
    left: 0;
    width: 100%;
    height: 28px;
    background: var(--maroon);
  }
  .band--top { top: 0; }
  .band--bottom { bottom: 0; }
  .ornament {
    position: absolute;
    background: radial-gradient(ellipse at center, rgba(42,28,12,0.55) 0%, rgba(42,28,12,0.25) 55%, rgba(42,28,12,0) 80%);
  }
  .ornament--left { left: 50px; top: 150px; width: 140px; height: 230px; }
  .ornament--right { right: 40px; top: 120px; width: 140px; height: 230px; }
  .brand {
    position: absolute;
    left: 90px;
    top: 58px;
    font-size: 30px;
    line-height: 1.15;
  }
  .owner {
    position: absolute;
    left: 215px;
    top: 150px;
    font-size: 40px;
  }
  .details {
    position: absolute;
    left: 390px;
    top: 250px;
    font-size: 21px;
    line-height: 1.35;
    list-style: none;
  }
</style>
</head>
<body>
  <main class="canvas">
    <section class="business-card" aria-label="Rahim's Kitchen business card">
      <div class="band band--top"></div>
      <div class="band band--bottom"></div>

      <div class="ornament ornament--left" role="img" aria-label="Arabic-style calligraphic ornament"></div>
      <div class="ornament ornament--right" role="img" aria-label="Arabic-style calligraphic ornament"></div>

      <header class="brand">
        <p class="brand__name">Rahim's Kitchen</p>
        <p class="brand__tagline">Authentic Kashmiri Indian Cuisine</p>
      </header>

      <p class="owner">Rahim Qureshi, Owner &amp; Chef</p>

      <ul class="details">
        <li>Takeaway Shop &amp; Catering</li>
        <li>BYO Function Room - Bookings Essential</li>
        <li>14 Marlow Lane, Ravenhill QLD</li>
        <li>07 5550 1842</li>
      </ul>
    </section>
  </main>
</body>
</html>
```